Wrap Design for a Box Truck and Cab

Greetings, Designers!

We're on the lookout for a talented Graphic Designer to craft a visually striking 4-sided wrap for a 2019 Varnel Box Truck and Cab Wrap. Here are the key details:

Design Elements:

Phone Number: (555) 284-7160
Website: www.fernwickchillsupply.example

Additional Information:
Feel free to unleash your creativity! While we've provided some imagery that you can use, it's not mandatory. We're open to various design styles and encourage you to be as imaginative as possible. Public feedback will be provided for the received designs. Also see the screenshot image of the vehicle, when designing, our ultimate goal is to have no yellow left, the cab may be a full color wrap or as a solid color change only.

Optional Content:
Consider incorporating the following optional elements, though they are not mandatory:
Delivery Area: North Dakota, South Dakota, Eastern Montana, and Minnesota.

This is an exciting opportunity to showcase your design prowess and contribute to the visual identity of Fernwick Chill Supply. We look forward to reviewing your innovative designs!

More wrap design projects will be available at a later date for: 4 door pickup truck, cargo van and car.

Please note, the website is in a redesign process and does not reflect the design of our company. The winning design should be mocked up on a Box Truck similar to the one shown, and winning designs will become property of Fernwick Chill Supply when completed.

Best regards,
Tobin

Target Market(s)

Business & Consumers of Dry Ice

Font styles to use
Sans Serif

Colors
0054AA
0677BA
7BADD7
CADEEF
E8F1F8
0094D4
00A9DD
6FCCEA
C7EBF8
E9F6FB

Requirements
Nice to have
• We like the colors of: Shades of Blue, White or Grey.

```html
<!DOCTYPE html>
<html lang="en">
<head>
<meta charset="utf-8">
<title>Fernwick Chill Supply – Box Truck Wrap</title>
<link rel="stylesheet" href="https://fonts.googleapis.com/css2?family=Montserrat:wght@400;600;700&display=swap">
<style>
  :root{
    --navy:#23339c;
    --royal:#1d4fb8;
    --brand-blue:#0677BA;
    --sky:#00A9DD;
    --ice:#6FCCEA;
    --frost:#C7EBF8;
    --snow:#E9F6FB;
    --white:#ffffff;
    --page:#ffffff;
  }
  *{margin:0;padding:0;box-sizing:border-box}
  html,body{width:1200px;height:736px;overflow:hidden;background:var(--page)}
  body{font-family:"Montserrat",Arial,sans-serif;position:relative}

  .wrap-side,.wrap-rear{position:absolute;overflow:hidden}
  .wrap-side{left:50px;top:212px;width:700px;height:313px;
    background:linear-gradient(100deg,var(--navy) 0%,var(--royal) 60%,var(--navy) 100%)}
  .wrap-rear{left:810px;top:212px;width:340px;height:315px;
    background:radial-gradient(ellipse at 50% 40%,var(--royal) 0%,var(--navy) 75%)}

  .delivery-bar{position:absolute;top:14px;left:30px;right:30px;display:flex;
    align-items:center;color:var(--white);font-size:8.5px;font-weight:700;letter-spacing:.4px}
  .delivery-bar .label{margin-right:44px}
  .delivery-bar .region{padding:0 22px;border-left:1px solid var(--sky)}
  .delivery-bar .region:first-of-type{border-left:none;padding-left:0}

  .frost-band{position:absolute;left:0;top:0;width:100%;height:100%}

  .product-art{position:absolute}
  .product-art.block{left:40px;top:108px;width:160px;height:110px;border-radius:10px;
    background:linear-gradient(160deg,var(--snow),var(--frost) 70%,var(--ice))}
  .product-art.scoop{left:505px;top:95px;width:170px;height:150px;border-radius:14px;
    background:linear-gradient(200deg,var(--ice),var(--snow) 45%,var(--royal))}

  .brand-name{position:absolute;text-align:center;font-weight:600;color:var(--brand-blue);
    letter-spacing:3px;line-height:1.1;text-transform:uppercase}
  .wrap-side .brand-name{left:200px;width:300px;top:104px;font-size:26px}
  .wrap-side .brand-url{position:absolute;left:200px;width:300px;top:176px;text-align:center;
    font-size:10px;color:#222;letter-spacing:.3px;text-transform:uppercase}

  .contact-row{position:absolute;right:14px;bottom:14px;display:flex;gap:18px;
    color:var(--white);font-weight:600;font-size:13px}
  .contact{display:flex;align-items:center;gap:6px}
  .icon-dot{width:18px;height:18px;border-radius:50%;background:var(--sky);
    display:flex;align-items:center;justify-content:center}

  .wrap-rear .brand-name{left:0;width:100%;top:64px;font-size:30px;color:var(--white)}
  .wrap-rear .brand-url{position:absolute;left:0;width:100%;top:142px;text-align:center;
    color:var(--white);font-size:11px;letter-spacing:.3px;text-transform:uppercase}
  .wrap-rear .phone{position:absolute;left:0;width:100%;top:193px;display:flex;
    justify-content:center;align-items:center;gap:8px;color:var(--white);font-weight:700;font-size:21px}
  .rear-frost{position:absolute;left:0;bottom:0;width:100%;height:64px;
    background:linear-gradient(180deg,var(--snow),var(--frost))}
  .url-pill{position:absolute;left:50%;transform:translateX(-50%);top:251px;
    background:var(--sky);color:var(--white);font-weight:700;font-size:10.5px;
    padding:3px 10px;white-space:nowrap}
</style>
</head>
<body>

<section class="wrap-side" aria-label="Side panel wrap">
  <svg class="frost-band" viewBox="0 0 700 313" preserveAspectRatio="none" aria-hidden="true">
    <defs>
      <linearGradient id="bandFill" x1="0" y1="0" x2="1" y2="0">
        <stop offset="0" stop-color="#C7EBF8"/>
        <stop offset=".35" stop-color="#ffffff"/>
        <stop offset=".7" stop-color="#ffffff"/>
        <stop offset="1" stop-color="#C7EBF8"/>
      </linearGradient>
    </defs>
    <path d="M0 80 C120 60 220 75 330 62 C450 48 560 55 700 38 L700 250 C580 262 470 245 350 258 C230 270 120 250 0 268 Z" fill="#6FCCEA" opacity=".7"/>
    <path d="M0 92 C120 74 230 88 340 76 C460 64 570 70 700 58 L700 232 C580 246 460 230 340 244 C220 256 110 238 0 252 Z" fill="url(#bandFill)"/>
  </svg>

  <div class="delivery-bar">
    <span class="label">DELIVERY AREA:</span>
    <span class="region">NORTH DAKOTA</span>
    <span class="region">SOUTH DAKOTA</span>
    <span class="region">EASTERN MONTANA</span>
    <span class="region">MINNESOTA</span>
  </div>

  <div class="product-art block" role="img" aria-label="Photo of a block of dry ice"></div>
  <div class="product-art scoop" role="img" aria-label="Photo of a scoop filled with dry ice pellets"></div>

  <div class="brand-name">Fernwick<br>Chill Supply</div>
  <div class="brand-url">fernwickchillsupply.example</div>

  <div class="contact-row">
    <span class="contact">
      <span class="icon-dot"><svg width="10" height="10" viewBox="0 0 24 24" aria-hidden="true"><path fill="#fff" d="M6.6 10.8a15 15 0 006.6 6.6l2.2-2.2a1 1 0 011-.25 11.4 11.4 0 003.6.57 1 1 0 011 1V20a1 1 0 01-1 1A17 17 0 013 4a1 1 0 011-1h3.5a1 1 0 011 1c0 1.25.2 2.45.57 3.57a1 1 0 01-.25 1z"/></svg></span>
      (555) 284-7160
    </span>
    <span class="contact">
      <span class="icon-dot"><svg width="10" height="10" viewBox="0 0 24 24" aria-hidden="true"><path fill="#fff" d="M5 2l14 11-6 1 3.5 7-2.5 1-3.5-7L5 19z"/></svg></span>
      www.fernwickchillsupply.example
    </span>
  </div>
</section>

<section class="wrap-rear" aria-label="Rear door wrap">
  <div class="brand-name">Fernwick<br>Chill Supply</div>
  <div class="brand-url">fernwickchillsupply.example</div>
  <div class="phone">
    <span class="icon-dot"><svg width="10" height="10" viewBox="0 0 24 24" aria-hidden="true"><path fill="#fff" d="M6.6 10.8a15 15 0 006.6 6.6l2.2-2.2a1 1 0 011-.25 11.4 11.4 0 003.6.57 1 1 0 011 1V20a1 1 0 01-1 1A17 17 0 013 4a1 1 0 011-1h3.5a1 1 0 011 1c0 1.25.2 2.45.57 3.57a1 1 0 01-.25 1z"/></svg></span>
    (555) 284-7160
  </div>
  <div class="rear-frost"></div>
  <div class="url-pill">www.fernwickchillsupply.example</div>
</section>

</body>
</html>
```